Business Card Design Project - Tall Maple

We are looking for a new business card design. Our company name is Tall Maple Communication Solutions. Our primary function is to provide our clients with communication solutions. These solutions include commercial phone systems and T1 and Fiber Internet lines. Another major part of the business is cabling new buildings with CAT5 cable for both data and phone.

Industry/Entity Type

Communication

Requirements
Must have
• The cards need to be two sided and have some bleeding edge color.
Nice to have
• We are going to upload our current logo BUT we are not married to this logo. If you want to incorporate a re-designed logo with the new business card - please feel free to do so. We are looking for a new bold look that is very colorful yet professional.

```html
<!DOCTYPE html>
<html lang="en">
<head>
<meta charset="utf-8">
<title>Tall Maple Communication Solutions – Business Card</title>
<link rel="stylesheet" href="https://fonts.googleapis.com/css2?family=Carlito&family=Alegreya+Sans:wght@400&display=swap">
<style>
  :root {
    --page: #ffffff;
    --card-front: #ffffff;
    --card-border: #3a1414;
    --card-back: #565b61;
    --back-edge: #d9a3a8;
    --ink-dark: #111111;
    --ink-light: #ece4ea;
  }
  html, body {
    margin: 0;
    padding: 0;
    width: 1200px;
    height: 989px;
    overflow: hidden;
    background: var(--page);
  }
  .canvas {
    position: relative;
    width: 1200px;
    height: 989px;
  }
  .card {
    position: absolute;
    left: 467px;
    width: 730px;
    box-sizing: border-box;
  }
  .card--front {
    top: 7px;
    height: 416px;
    background: var(--card-front);
    border: 2px solid var(--card-border);
  }
  .card--back {
    top: 572px;
    height: 417px;
    background: var(--card-back);
    border-left: 1px solid var(--back-edge);
  }
  .brand {
    margin: 0;
    font-family: "Carlito", "Calibri", sans-serif;
    font-weight: 400;
    color: var(--ink-dark);
  }
  .brand__name,
  .brand__tagline {
    position: absolute;
    left: 182px;
    line-height: 1;
    white-space: nowrap;
  }
  .brand__name {
    top: 303px;
    font-size: 43px;
  }
  .brand__tagline {
    top: 350px;
    font-size: 35px;
  }
  .contact {
    position: absolute;
    left: 182px;
    top: 133px;
    margin: 0;
    font-family: "Alegreya Sans", "Corbel", sans-serif;
    font-size: 26px;
    line-height: 32px;
    color: var(--ink-light);
    font-style: normal;
    white-space: nowrap;
  }
  .contact__block { margin: 0; }
  .contact__block + .contact__block { margin-top: 36px; }
  .contact__line { display: block; }
</style>
</head>
<body>
<main class="canvas">
  <section class="card card--front" aria-label="Card front">
    <h1 class="brand">
      <span class="brand__name">Tall Maple</span>
      <span class="brand__tagline">Communication Solutions</span>
    </h1>
  </section>

  <section class="card card--back" aria-label="Card back">
    <address class="contact">
      <p class="contact__block">
        <span class="contact__line">Dorian Westfall</span>
        <span class="contact__line">1840 N Juniper Avenue Suite 410</span>
        <span class="contact__line">Mesa, AZ 85203</span>
      </p>
      <p class="contact__block">
        <span class="contact__line">480.555.0142 Office</span>
        <span class="contact__line">480.555.0187 Mobile</span>
        <span class="contact__line">800.555.0119 24/7</span>
        <span class="contact__line">800.555.0163 Fax</span>
      </p>
    </address>
  </section>
</main>
</body>
</html>
```